New business card, letter head, email signature and Portfolio for our Security company.

We are an Vantage security company that provides a top quality manpower services to protect high rise buildings, retail and all type of properties and would like a new business card/logo look.

- We would like the spot UV design.
- Matt black (double sided).
- We would like to incorporate a royal blue colour (feel free to experiment with it).
- Feel free to try different lengths with the card to make it stand out more than a normal business card.
- We would like the logo to be an eagle eye in the background (shines when card is tilted slightly in the background, either on the front, back or both sides of the card). Image attached as an example of eye shape (colour to be either black or royal blue).
- MARLOW VANTAGE GUARD AGENCY PTY. LTD. and MVGA to be placed on one side of the card and on the other side of the card to have;

- Name in slightly bigger font than the position (directly on the bottom on the name).
- Mobile number
- Email address
- Website email address
- PO BOX address

Can we please have the files in a format that we can edit.

Reason: I need to consult my business partner with the designs so far and will make a decision from there.

Target Market(s)

Security Industry

Industry/Entity Type

Business

Contact Information for Business Card

- Mobile number
- Email address
- Website email address
- PO BOX address

Logo Text

MVGA and underneath the MVGA please add MARLOW VANTAGE GUARD AGENCY PTY. LTD.

Font styles to use
Other font styles liked:
• bold type font

Colors
0255a3
000000

Requirements
Must have
• We are an Vantage security company that provides a top quality manpower services to protect high rise buildings, retail and all type of properties and would like a new business card/logo look.
• - We would like the spot UV design.
• - Matt black (double sided).
• - We would like to incorporate a royal blue colour (feel free to experiment with it).
• - Feel free to try different lengths with the card to make it stand out more than a normal business card.
• - We would like the logo to be an eagle eye in the background (shines when card is tilted slightly in the background, either on the front, back or both sides of the card). Image attached as an example of eye shape (colour to be either black or royal blue).
• - MARLOW VANTAGE GUARD AGENCY PTY. LTD. and MVGA to be placed on one side of the card and on the other side of the card to have;
• - Name in slightly bigger font than the position (directly on the bottom on the name).
• - Mobile number
• - Email address
• - Website email address
• - PO BOX address
• Can we please have the files in a format that we can edit.
Nice to have
• Feel free to try different lengths with the card to make it stand out more than a normal business card.
• Please find "URBAN JUNGLE" font attached and incorporate MVGA into the same style with building's inside the MVGA bold front also add MARLOW into the bottom part of the S and follow on E - Vantage on the bottom S - SECURITY on the bottom S - SERVICES on the bottom of each letter.
• other than that, I'll be happy with a bold modern font for the MVGA and MARLOW VANTAGE GUARD AGENCY in a bold and thinner font underneath.

```html
<!DOCTYPE html>
<html lang="en">
<head>
<meta charset="utf-8">
<title>Marlow Vantage Guard Agency – Business Card</title>
<link rel="stylesheet" href="https://fonts.googleapis.com/css2?family=Open+Sans:wght@400;600;700;800&display=swap">
<style>
  :root {
    --royal-blue: #0255a3;
    --ink: #000000;
    --matte-black: #141414;
    --uv-grey: #a8a8a8;
    --paper: #ffffff;
    --stage: #3a3431;
    --rule: #9a9a9a;
  }
  * { box-sizing: border-box; margin: 0; padding: 0; }
  html, body {
    width: 1200px; height: 780px; overflow: hidden;
    background: var(--stage);
    font-family: "Open Sans", Verdana, sans-serif;
  }
  .canvas {
    width: 1200px; height: 780px;
    display: flex; align-items: center; justify-content: center; gap: 40px;
  }
  .card {
    width: 540px; height: 310px;
    position: relative;
    box-shadow: 0 12px 30px rgba(0,0,0,.45);
  }
  .card--front { background: var(--matte-black); }
  .card--back { background: var(--paper); }

  .brand { display: flex; flex-direction: column; align-items: center; }
  .brand__mark {
    font-weight: 800; font-size: 96px; line-height: 1; letter-spacing: 4px;
  }
  .brand__name {
    font-weight: 600; font-size: 15.5px; letter-spacing: .5px; margin-top: 6px;
    text-transform: uppercase;
  }
  .card--front .brand {
    position: absolute; left: 0; right: 0; top: 88px;
  }
  .card--front .brand__mark, .card--front .brand__name { color: var(--uv-grey); }

  .card--back .brand {
    position: absolute; left: 22px; top: 94px; width: 252px;
  }
  .card--back .brand__mark { font-size: 72px; color: var(--ink); letter-spacing: 3px; }
  .card--back .brand__name { font-size: 11px; color: var(--ink); letter-spacing: .2px; }

  .divider {
    position: absolute; left: 290px; top: 70px; width: 1px; height: 170px;
    background: var(--rule);
  }
  .contact { position: absolute; left: 310px; top: 78px; color: var(--ink); }
  .contact__name { font-weight: 600; font-size: 21px; line-height: 1.1; }
  .contact__role { font-size: 13px; color: var(--royal-blue); margin-bottom: 14px; }
  .contact__list { list-style: none; }
  .contact__item {
    display: flex; align-items: center; gap: 8px;
    font-size: 13px; line-height: 22px;
  }
  .contact__icon {
    width: 16px; height: 16px; flex: none;
    background: var(--royal-blue); border-radius: 2px;
    display: flex; align-items: center; justify-content: center;
  }
  .contact__address { font-size: 13px; line-height: 18px; margin-top: 6px; font-style: normal; }
</style>
</head>
<body>
<main class="canvas">
  <section class="card card--front" aria-label="Card front">
    <div class="brand">
      <div class="brand__mark">MVGA</div>
      <div class="brand__name">Marlow Vantage Guard Agency</div>
    </div>
  </section>

  <section class="card card--back" aria-label="Card back">
    <div class="brand">
      <div class="brand__mark">MVGA</div>
      <div class="brand__name">Marlow Vantage Guard Agency</div>
    </div>
    <div class="divider"></div>
    <div class="contact">
      <h1 class="contact__name">Employee Name</h1>
      <p class="contact__role">Manager</p>
      <ul class="contact__list">
        <li class="contact__item">
          <span class="contact__icon">
            <svg width="10" height="12" viewBox="0 0 10 12"><rect x="1.5" y="0.5" width="7" height="11" rx="1.2" fill="none" stroke="#fff"/><rect x="3" y="2" width="4" height="5" fill="#fff"/></svg>
          </span>0400 318 262
        </li>
        <li class="contact__item">
          <span class="contact__icon">
            <svg width="12" height="9" viewBox="0 0 12 9"><rect x="0.5" y="0.5" width="11" height="8" fill="none" stroke="#fff"/><path d="M0.5 0.5 L6 5 L11.5 0.5" fill="none" stroke="#fff"/></svg>
          </span>contact@marlowvantage.net.nz
        </li>
        <li class="contact__item">
          <span class="contact__icon">
            <svg width="12" height="12" viewBox="0 0 12 12" fill="none" stroke="#fff"><circle cx="6" cy="6" r="5"/><ellipse cx="6" cy="6" rx="2.2" ry="5"/><path d="M1 6 H11"/></svg>
          </span>www.marlowvantage.co.nz
        </li>
      </ul>
      <address class="contact__address">P.O. Box 417, Kestrel Lane<br>Harrow Bay, New Zealand</address>
    </div>
  </section>
</main>
</body>
</html>
```